Travel Blogger Business Card for roamquill.net

I need a two-sided business card for a travel blogging website. The card should be both professional and fun at the same time. This is for the website www.roamquill.net

I don't necessarily think that the current logo on the website needs to be used on the business card but it can be. I am very flexible with ideas

Target Market(s)

Travel agencies that will be met at a conference.

Industry/Entity Type

Travel

Contact Information for Business Card

Company Name: Roam Quill.net
Name: Bertrand Olesky
Voice: +1-(345)-402-7731
Address: Coral Reach Shore, Grand Cayman, Cayman Islands
Email: ceo@roamquill.net

Colors
0592cd
0355a3
3176b5
33a6d7
85cae6
85acd3

Requirements
Must have
• Website address and name should be bigger than address, phone number, and email.

```html
<!DOCTYPE html>
<html lang="en">
<head>
<meta charset="utf-8">
<title>Roam Quill – Business Card</title>
<link rel="stylesheet" href="https://fonts.googleapis.com/css2?family=Lilita+One&display=swap">
<style>
  :root{
    --backdrop:#e6dde2;
    --rim:#1a93d6;
    --sky-blue:#33a6d7;
    --mid-blue:#0592cd;
    --water:#3176b5;
    --deep-blue:#0355a3;
    --pale-blue:#85cae6;
    --sunset:#e8731f;
    --sunset-light:#f0a040;
    --cream:#efe6d6;
  }
  *{margin:0;padding:0;box-sizing:border-box}
  html,body{width:1200px;height:1200px;overflow:hidden;background:var(--backdrop)}
  .canvas{position:relative;width:1200px;height:1200px}
  .card-shapes{position:absolute;inset:0}
  .card-text{
    position:absolute;left:0;width:1200px;text-align:center;
    font-family:"Lilita One",sans-serif;color:var(--cream);line-height:1;
  }
  .brand-name{top:270px;font-size:86px;letter-spacing:3px}
  .tagline{top:420px;font-size:40px}
  .person-name{top:740px;font-size:42px}
  .website{top:794px;font-size:42px}
  .contact-line{font-size:19px;letter-spacing:.3px}
  .contact-phone{top:901px}
  .contact-address{top:938px}
  .contact-email{top:975px}
</style>
</head>
<body>
<div class="canvas">
  <svg class="card-shapes" width="1200" height="1200" viewBox="0 0 1200 1200">
    <defs>
      <path id="badge" d="M600 72 L900 200 Q930 215 920 240 Q946 272 946 315 Q946 360 920 395 Q930 420 900 440 L600 556 L300 440 Q270 420 280 395 Q254 360 254 315 Q254 272 280 240 Q270 215 300 200 Z"/>
      <linearGradient id="sunsetGlow" x1="0" y1="0" x2="0" y2="1">
        <stop offset="0" stop-color="var(--sunset-light)"/>
        <stop offset="1" stop-color="var(--sunset)"/>
      </linearGradient>
      <linearGradient id="ridgeShade" x1="0" y1="0" x2="0" y2="1">
        <stop offset="0" stop-color="#3a2a20" stop-opacity="0"/>
        <stop offset="1" stop-color="#2a1f18"/>
      </linearGradient>
      <clipPath id="frontInner"><path d="M600 88 L890 212 Q915 225 906 246 Q930 275 930 315 Q930 358 906 390 Q915 412 890 428 L600 540 L310 428 Q285 412 294 390 Q270 358 270 315 Q270 275 294 246 Q285 225 310 212 Z"/></clipPath>
      <clipPath id="backInner"><path transform="translate(0 562)" d="M600 88 L890 212 Q915 225 906 246 Q930 275 930 315 Q930 358 906 390 Q915 412 890 428 L600 540 L310 428 Q285 412 294 390 Q270 358 270 315 Q270 275 294 246 Q285 225 310 212 Z"/></clipPath>
    </defs>

    <!-- front side -->
    <g class="card-front">
      <use href="#badge" fill="var(--rim)"/>
      <g clip-path="url(#frontInner)">
        <rect x="254" y="72" width="692" height="484" fill="var(--mid-blue)"/>
        <rect x="254" y="72" width="692" height="168" fill="url(#sunsetGlow)" role="img" aria-label="Sunburst behind a mountain range with a winding trail"/>
        <rect x="254" y="190" width="692" height="50" fill="url(#ridgeShade)" opacity=".85"/>
        <rect x="254" y="240" width="692" height="150" fill="var(--sky-blue)"/>
        <rect x="254" y="320" width="692" height="70" fill="var(--pale-blue)" opacity=".18" role="img" aria-label="Pine forest silhouette along the shoreline"/>
        <path d="M254 390 Q600 384 946 390 L946 470 L254 470 Z" fill="var(--water)" role="img" aria-label="Lake water with small fish"/>
        <path d="M254 470 L946 470 L946 556 L254 556 Z" fill="var(--deep-blue)" opacity=".6"/>
        <path d="M544 528 A56 56 0 0 1 656 528 Z" fill="var(--sunset)"/>
      </g>
    </g>

    <!-- back side -->
    <g class="card-back">
      <use href="#badge" y="562" fill="var(--rim)"/>
      <g clip-path="url(#backInner)">
        <rect x="254" y="634" width="692" height="484" fill="var(--mid-blue)"/>
        <path d="M600 684 L876 756 L324 756 Z" fill="#2ab8e0"/>
        <rect x="254" y="790" width="692" height="84" fill="var(--pale-blue)" opacity=".18" role="img" aria-label="Pine forest silhouette"/>
        <rect x="254" y="800" width="692" height="74" fill="var(--sky-blue)" opacity=".7"/>
        <rect x="300" y="874" width="600" height="166" fill="var(--deep-blue)"/>
        <path d="M300 1000 L600 1040 L900 1000 L900 1118 L300 1118 Z" fill="var(--water)" opacity=".6"/>
      </g>
    </g>
  </svg>

  <div class="card-text brand-name">ROAM QUILL</div>
  <div class="card-text tagline">Blog Site</div>

  <div class="card-text person-name">Bertrand Olesky</div>
  <div class="card-text website">Roam Quill.net</div>
  <div class="card-text contact-line contact-phone">+1-(345)-402-7731</div>
  <div class="card-text contact-line contact-address">Coral Reach Shore, Grand Cayman, Cayman Islands</div>
  <div class="card-text contact-line contact-email">ceo@roamquill.net</div>
</div>
</body>
</html>
```